Design for a 4 screens iOS and Android app - "VelidMetra"

The app allows you to track your car gasoline refill ...
We need a design for the 4 screens of the app:
a) 1 form with 3 fields.
b) 1 simple list view
c) 1 summary view
d) 1 text page
2 "alerts" items are also to be designed.
No specific guidelines, nor logo or whatever.
It will be a free app distributed on iOS and Androïd.
We just want to make it looking nice & very usable for end users.
Target Market(s)
B2C app
Industry/Entity Type
Android

```html
<!DOCTYPE html>
<html lang="en">
<head>
<meta charset="utf-8">
<title>VelidMetra – App Screens</title>
<link href="https://fonts.googleapis.com/css2?family=Inter:wght@300;400;500;600&display=swap" rel="stylesheet">
<style>
  :root {
    --canvas: #f3f3f3;
    --screen: #1a1f25;
    --status: #1c2127;
    --header: #1f262d;
    --card: #222b33;
    --divider: #3a444d;
    --text: #ffffff;
    --muted: #c9ced3;
    --tab-icon: #2f86e8;
    --tab-label: #8a949d;
    --accent: #0a7cff;
    --save: #f65b5a;
    --clear: #4a5057;
  }
  * { box-sizing: border-box; margin: 0; padding: 0; }
  html, body { width: 1200px; height: 1000px; overflow: hidden; }
  body { background: var(--canvas); font-family: "Inter", "Helvetica Neue", Arial, sans-serif; color: var(--text); position: relative; }

  .screen { position: absolute; top: 208px; width: 284px; height: 504px; background: var(--screen); overflow: hidden; }
  .screen--add { left: 22px; }
  .screen--list { left: 312px; }
  .screen--stats { left: 602px; }
  .screen--about { left: 892px; }

  .status-bar { position: absolute; top: 0; left: 0; right: 0; height: 16px; background: var(--status); font-size: 8px; font-weight: 500; display: flex; align-items: center; justify-content: space-between; padding: 0 5px; }
  .status-bar__left, .status-bar__right { display: flex; align-items: center; gap: 3px; width: 80px; }
  .status-bar__right { justify-content: flex-end; }
  .status-bar__time { font-weight: 600; }
  .signal { letter-spacing: -1px; font-size: 6px; }
  .battery { width: 17px; height: 7px; border: 1px solid #fff; border-radius: 1.5px; padding: 1px; position: relative; }
  .battery::before { content: ""; display: block; width: 100%; height: 100%; background: #fff; }
  .battery::after { content: ""; position: absolute; right: -3px; top: 1.5px; width: 1.5px; height: 2.5px; background: #fff; }

  .header { position: absolute; top: 16px; left: 0; right: 0; height: 32px; background: var(--header); display: flex; align-items: center; justify-content: center; font-size: 12.5px; font-weight: 500; }
  .screen--add .header { background: var(--screen); font-size: 11px; font-weight: 400; }

  /* Add form */
  .field { position: absolute; left: 0; right: 0; height: 107px; text-align: center; }
  .field__value { position: absolute; left: 0; right: 0; top: 0; font-size: 32px; font-weight: 300; line-height: 40px; }
  .field__label { position: absolute; left: 0; right: 0; top: 40px; font-size: 13px; line-height: 16px; }
  .field__chevron { position: absolute; left: 133px; top: 59px; }
  .field__clear { position: absolute; left: 237px; top: 9px; }
  .field__divider { position: absolute; left: 13px; right: 18px; top: 77px; height: 1px; background: var(--divider); }
  .save-button { position: absolute; left: 0; right: 0; top: 407px; height: 45px; background: var(--save); font-size: 17px; display: flex; align-items: center; justify-content: center; }

  /* Record list */
  .segmented { position: absolute; left: 85px; top: 54px; width: 114px; height: 21px; border: 1px solid #fff; border-radius: 3px; display: flex; font-size: 9px; overflow: hidden; }
  .segmented__item { flex: 1; display: flex; align-items: center; justify-content: center; }
  .segmented__item--active { background: #fff; color: var(--accent); }
  .record { position: absolute; left: 6px; width: 272px; height: 75px; background: var(--card); padding: 0 8px; }
  .record__top, .record__bottom { position: absolute; left: 8px; right: 8px; display: flex; justify-content: space-between; font-size: 13px; line-height: 16px; }
  .record__top { top: 12px; }
  .record__rule { position: absolute; left: 8px; right: 8px; top: 37px; height: 1px; background: var(--divider); }
  .record__bottom { top: 44px; }
  .record__litres { position: absolute; left: 95px; }

  /* Monthly usage */
  .month { position: absolute; left: 6px; width: 271px; height: 120px; background: var(--card); }
  .month__title { position: absolute; left: 8px; top: 10px; font-size: 13px; line-height: 16px; }
  .month__rule { position: absolute; left: 8px; right: 10px; top: 35px; height: 1px; background: var(--divider); }
  .month__stats { position: absolute; left: 8px; right: 10px; top: 42px; font-size: 12.5px; line-height: 16.4px; }
  .month__row { display: flex; justify-content: space-between; }
  .month__row dd { color: var(--muted); }

  /* About */
  .about__text { position: absolute; left: 8px; right: 8px; top: 72px; text-align: center; font-size: 12px; font-weight: 500; line-height: 15.4px; }
  .about__link { position: absolute; left: 0; right: 0; top: 302px; text-align: center; font-size: 12px; font-weight: 500; color: var(--accent); }

  /* Tab bar */
  .tab-bar { position: absolute; left: 0; right: 0; bottom: 0; height: 52px; background: var(--header); display: flex; z-index: 2; }
  .tab { flex: 1; position: relative; display: flex; flex-direction: column; align-items: center; color: var(--tab-label); font-size: 7px; }
  .tab svg { position: absolute; top: 12px; }
  .tab span { position: absolute; bottom: 3px; }
  .tab--active { background: var(--accent); color: #fff; }
</style>
</head>
<body>

<!-- Add screen -->
<section class="screen screen--add">
  <div class="status-bar">
    <div class="status-bar__left"><span class="signal">●●●●●</span><span>Nimbus</span>
      <svg width="9" height="7" viewBox="0 0 9 7"><path d="M0.5 2.5a5.5 5.5 0 0 1 8 0M2 4a3.4 3.4 0 0 1 5 0" stroke="#fff" fill="none" stroke-width="1"/><circle cx="4.5" cy="5.8" r="0.9" fill="#fff"/></svg></div>
    <div class="status-bar__time">9:41 AM</div>
    <div class="status-bar__right"><span>100%</span><span class="battery"></span></div>
  </div>
  <div class="header">21 February 2016</div>

  <div class="field" style="top:77px">
    <div class="field__value">1200</div>
    <div class="field__label">Kilometres</div>
    <svg class="field__chevron" width="18" height="10" viewBox="0 0 18 10"><path d="M1 1l8 8 8-8" stroke="#fff" fill="none" stroke-width="1.2"/></svg>
    <svg class="field__clear" width="22" height="22" viewBox="0 0 22 22"><circle cx="11" cy="11" r="11" fill="var(--clear)"/><path d="M7.5 7.5l7 7M14.5 7.5l-7 7" stroke="#fff" stroke-width="1.1"/></svg>
    <div class="field__divider"></div>
  </div>
  <div class="field" style="top:184px">
    <div class="field__value">30</div>
    <div class="field__label">Litres</div>
    <svg class="field__chevron" width="18" height="10" viewBox="0 0 18 10"><path d="M1 1l8 8 8-8" stroke="#fff" fill="none" stroke-width="1.2"/></svg>
    <svg class="field__clear" width="22" height="22" viewBox="0 0 22 22"><circle cx="11" cy="11" r="11" fill="var(--clear)"/><path d="M7.5 7.5l7 7M14.5 7.5l-7 7" stroke="#fff" stroke-width="1.1"/></svg>
    <div class="field__divider"></div>
  </div>
  <div class="field" style="top:292px">
    <div class="field__value">€ 120</div>
    <div class="field__label">Euros</div>
    <svg class="field__chevron" width="18" height="10" viewBox="0 0 18 10"><path d="M1 1l8 8 8-8" stroke="#fff" fill="none" stroke-width="1.2"/></svg>
    <svg class="field__clear" width="22" height="22" viewBox="0 0 22 22"><circle cx="11" cy="11" r="11" fill="var(--clear)"/><path d="M7.5 7.5l7 7M14.5 7.5l-7 7" stroke="#fff" stroke-width="1.1"/></svg>
  </div>

  <div class="save-button">Save</div>

  <nav class="tab-bar">
    <div class="tab tab--active"><svg width="22" height="22" viewBox="0 0 22 22"><path d="M11 1v20M1 11h20" stroke="#fff" stroke-width="1.1"/></svg><span>Add</span></div>
    <div class="tab"><svg width="22" height="22" viewBox="0 0 22 22"><g stroke="var(--tab-icon)" stroke-width="1"><path d="M5 5h16M5 11h16M5 17h16M1 5h2M1 11h2M1 17h2"/></g></svg><span>List</span></div>
    <div class="tab"><svg width="22" height="22" viewBox="0 0 22 22"><polyline points="2,17 8,11 13,14 20,6" fill="none" stroke="var(--tab-icon)" stroke-width="1"/><g fill="var(--tab-icon)"><circle cx="2" cy="17" r="1.6"/><circle cx="8" cy="11" r="1.6"/><circle cx="13" cy="14" r="1.6"/><circle cx="20" cy="6" r="1.6"/></g></svg><span>Statistic</span></div>
    <div class="tab"><svg width="22" height="22" viewBox="0 0 22 22"><circle cx="11" cy="11" r="10" fill="none" stroke="var(--tab-icon)" stroke-width="1"/><path d="M11 9v7" stroke="var(--tab-icon)" stroke-width="1.1"/><circle cx="11" cy="6.3" r="0.9" fill="var(--tab-icon)"/></svg><span>About Us</span></div>
  </nav>
</section>

<!-- Record list screen -->
<section class="screen screen--list">
  <div class="status-bar">
    <div class="status-bar__left"><span class="signal">●●●●●</span><span>Nimbus</span>
      <svg width="9" height="7" viewBox="0 0 9 7"><path d="M0.5 2.5a5.5 5.5 0 0 1 8 0M2 4a3.4 3.4 0 0 1 5 0" stroke="#fff" fill="none" stroke-width="1"/><circle cx="4.5" cy="5.8" r="0.9" fill="#fff"/></svg></div>
    <div class="status-bar__time">9:41 AM</div>
    <div class="status-bar__right"><span>100%</span><span class="battery"></span></div>
  </div>
  <div class="header" style="height:70px;align-items:flex-start;padding-top:10px">Record List</div>
  <div class="segmented"><div class="segmented__item segmented__item--active">All</div><div class="segmented__item">Today</div></div>

  <article class="record" style="top:86px"><div class="record__top"><span>14 February 2016</span><span>14:00</span></div><div class="record__rule"></div><div class="record__bottom"><span>127000 Km</span><span class="record__litres">49 Litres</span><span>€ 120</span></div></article>
  <article class="record" style="top:168px"><div class="record__top"><span>14 February 2016</span><span>14:00</span></div><div class="record__rule"></div><div class="record__bottom"><span>127000 Km</span><span class="record__litres">49 Litres</span><span>€ 120</span></div></article>
  <article class="record" style="top:249px"><div class="record__top"><span>14 February 2016</span><span>14:00</span></div><div class="record__rule"></div><div class="record__bottom"><span>127000 Km</span><span class="record__litres">49 Litres</span><span>€ 120</span></div></article>
  <article class="record" style="top:330px"><div class="record__top"><span>14 February 2016</span><span>14:00</span></div><div class="record__rule"></div><div class="record__bottom"><span>127000 Km</span><span class="record__litres">49 Litres</span><span>€ 120</span></div></article>
  <article class="record" style="top:411px"><div class="record__top"><span>14 February 2016</span><span>14:00</span></div><div class="record__rule"></div><div class="record__bottom"><span>127000 Km</span><span class="record__litres">49 Litres</span><span>€ 120</span></div></article>

  <nav class="tab-bar">
    <div class="tab"><svg width="22" height="22" viewBox="0 0 22 22"><path d="M11 1v20M1 11h20" stroke="var(--tab-icon)" stroke-width="1.1"/></svg><span>Add</span></div>
    <div class="tab tab--active"><svg width="22" height="22" viewBox="0 0 22 22"><g stroke="#fff" stroke-width="1"><path d="M5 5h16M5 11h16M5 17h16M1 5h2M1 11h2M1 17h2"/></g></svg><span>List</span></div>
    <div class="tab" style="color:#fff"><svg width="22" height="22" viewBox="0 0 22 22"><polyline points="2,17 8,11 13,14 20,6" fill="none" stroke="var(--tab-icon)" stroke-width="1"/><g fill="var(--tab-icon)"><circle cx="2" cy="17" r="1.6"/><circle cx="8" cy="11" r="1.6"/><circle cx="13" cy="14" r="1.6"/><circle cx="20" cy="6" r="1.6"/></g></svg><span>Statistic</span></div>
    <div class="tab" style="color:#fff"><svg width="22" height="22" viewBox="0 0 22 22"><circle cx="11" cy="11" r="10" fill="none" stroke="var(--tab-icon)" stroke-width="1"/><path d="M11 9v7" stroke="var(--tab-icon)" stroke-width="1.1"/><circle cx="11" cy="6.3" r="0.9" fill="var(--tab-icon)"/></svg><span>About Us</span></div>
  </nav>
</section>

<!-- Monthly usage screen -->
<section class="screen screen--stats">
  <div class="status-bar">
    <div class="status-bar__left"><span class="signal">●●●●●</span><span>Nimbus</span>
      <svg width="9" height="7" viewBox="0 0 9 7"><path d="M0.5 2.5a5.5 5.5 0 0 1 8 0M2 4a3.4 3.4 0 0 1 5 0" stroke="#fff" fill="none" stroke-width="1"/><circle cx="4.5" cy="5.8" r="0.9" fill="#fff"/></svg></div>
    <div class="status-bar__time">9:41 AM</div>
    <div class="status-bar__right"><span>100%</span><span class="battery"></span></div>
  </div>
  <div class="header">Monthly Usage</div>

  <article class="month" style="top:56px">
    <h2 class="month__title" style="font-weight:400">February 2016</h2><div class="month__rule"></div>
    <dl class="month__stats"><div class="month__row"><dt>Total Cost</dt><dd>570.54 €</dd></div><div class="month__row"><dt>Mileage</dt><dd>7500 Km</dd></div><div class="month__row"><dt>Full Tanks</dt><dd>11 L</dd></div><div class="month__row"><dt>Consumption</dt><dd>6.5 L</dd></div></dl>
  </article>
  <article class="month" style="top:182px">
    <h2 class="month__title" style="font-weight:400">January 2016</h2><div class="month__rule"></div>
    <dl class="month__stats"><div class="month__row"><dt>Total Cost</dt><dd>570.54 €</dd></div><div class="month__row"><dt>Mileage</dt><dd>7500 Km</dd></div><div class="month__row"><dt>Full Tanks</dt><dd>11 L</dd></div><div class="month__row"><dt>Consumption</dt><dd>6.5 L</dd></div></dl>
  </article>
  <article class="month" style="top:308px">
    <h2 class="month__title" style="font-weight:400">Decembre 2015</h2><div class="month__rule"></div>
    <dl class="month__stats"><div class="month__row"><dt>Total Cost</dt><dd>570.54 €</dd></div><div class="month__row"><dt>Mileage</dt><dd>7500 Km</dd></div><div class="month__row"><dt>Full Tanks</dt><dd>11 L</dd></div><div class="month__row"><dt>Consumption</dt><dd>6.5 L</dd></div></dl>
  </article>

  <nav class="tab-bar">
    <div class="tab"><svg width="22" height="22" viewBox="0 0 22 22"><path d="M11 1v20M1 11h20" stroke="var(--tab-icon)" stroke-width="1.1"/></svg><span>Add</span></div>
    <div class="tab"><svg width="22" height="22" viewBox="0 0 22 22"><g stroke="var(--tab-icon)" stroke-width="1"><path d="M5 5h16M5 11h16M5 17h16M1 5h2M1 11h2M1 17h2"/></g></svg><span>List</span></div>
    <div class="tab tab--active"><svg width="22" height="22" viewBox="0 0 22 22"><polyline points="2,17 8,11 13,14 20,6" fill="none" stroke="#fff" stroke-width="1"/><g fill="#fff"><circle cx="2" cy="17" r="1.6"/><circle cx="8" cy="11" r="1.6"/><circle cx="13" cy="14" r="1.6"/><circle cx="20" cy="6" r="1.6"/></g></svg><span>Statistic</span></div>
    <div class="tab" style="color:#fff"><svg width="22" height="22" viewBox="0 0 22 22"><circle cx="11" cy="11" r="10" fill="none" stroke="var(--tab-icon)" stroke-width="1"/><path d="M11 9v7" stroke="var(--tab-icon)" stroke-width="1.1"/><circle cx="11" cy="6.3" r="0.9" fill="var(--tab-icon)"/></svg><span>About Us</span></div>
  </nav>
</section>

<!-- About screen -->
<section class="screen screen--about">
  <div class="status-bar">
    <div class="status-bar__left"><span class="signal">●●●●●</span><span>Nimbus</span>
      <svg width="9" height="7" viewBox="0 0 9 7"><path d="M0.5 2.5a5.5 5.5 0 0 1 8 0M2 4a3.4 3.4 0 0 1 5 0" stroke="#fff" fill="none" stroke-width="1"/><circle cx="4.5" cy="5.8" r="0.9" fill="#fff"/></svg></div>
    <div class="status-bar__time">9:41 AM</div>
    <div class="status-bar__right"><span>100%</span><span class="battery"></span></div>
  </div>
  <div class="header">About Us</div>

  <p class="about__text">Lorem Ipsum is simply dummy text of the<br>printing and typesetting industry. Lorem<br>Ipsum has been the industry's standard<br>dummy text ever since the 1500s, when an<br>unknown printer took a galley of type and<br>scrambled it to make a type specimen book.<br>It has survived not only five centuries, but<br>also the leap into electronic typesetting,<br>remaining essentially unchanged. It was<br>popularised in the 1960s with the release<br>of Lettrix sheets containing Lorem Ipsum<br>passages, and more recently with desktop<br>publishing software like Alden PageBuilder<br>including versions of Lorem Ipsum.</p>
  <p class="about__link">www.fuelnotes-example.com</p>

  <nav class="tab-bar">
    <div class="tab" style="color:#fff"><svg width="22" height="22" viewBox="0 0 22 22"><path d="M11 1v20M1 11h20" stroke="var(--tab-icon)" stroke-width="1.1"/></svg><span>Add</span></div>
    <div class="tab" style="color:#fff"><svg width="22" height="22" viewBox="0 0 22 22"><g stroke="var(--tab-icon)" stroke-width="1"><path d="M5 5h16M5 11h16M5 17h16M1 5h2M1 11h2M1 17h2"/></g></svg><span>List</span></div>
    <div class="tab"><svg width="22" height="22" viewBox="0 0 22 22"><polyline points="2,17 8,11 13,14 20,6" fill="none" stroke="var(--tab-icon)" stroke-width="1"/><g fill="var(--tab-icon)"><circle cx="2" cy="17" r="1.6"/><circle cx="8" cy="11" r="1.6"/><circle cx="13" cy="14" r="1.6"/><circle cx="20" cy="6" r="1.6"/></g></svg><span>Statistic</span></div>
    <div class="tab tab--active"><svg width="22" height="22" viewBox="0 0 22 22"><circle cx="11" cy="11" r="10" fill="none" stroke="#fff" stroke-width="1"/><path d="M11 9v7" stroke="#fff" stroke-width="1.1"/><circle cx="11" cy="6.3" r="0.9" fill="#fff"/></svg><span>About Us</span></div>
  </nav>
</section>

</body>
</html>
```